Leave-behind marketing postcard showing retirement plan limits for the last three years.

We need a 5x7 postcard for our company, Bellwether Pension Group, Inc. We are a third party retirement plan administration firm. The piece should include our logo, address, phone, website, and the contribution limits for the last three years - 2015, 2014, 2013 (see attached for company logo, color palette and retirement plan limits chart). You can also incorporate our slogan on one of the sides - "Providing and protecting retirement since 1983." This postcard is a leave-behind. We will not be mailing it so you don't have to include space for a stamp and address. The postcard can be 4 color on both sides. Include a bleed.

Target Market(s)

Financial advisors and business owners

Industry/Entity Type

Marketing

Font styles to use
Other font styles liked:
• Georgia and arial

Requirements
Must have
• Please use some of the colors in the attached color palette.

```html
<!DOCTYPE html>
<html lang="en">
<head>
<meta charset="utf-8">
<title>Bellwether Pension Group, Inc. – Retirement Plan Limits</title>
<link rel="stylesheet" href="https://fonts.googleapis.com/css2?family=Arimo:wght@400;700&family=Gelasio:wght@400&display=swap">
<style>
  :root {
    --backdrop: #0a0d10;
    --gold: #f0b414;
    --navy-ink: #14163f;
    --heading-ink: #1c2c5a;
    --mist: #d3d6d8;
    --ocean: #02527e;
    --teal: #6fafb5;
    --taupe: #b4a7a1;
    --white: #ffffff;
    --rule: #111111;
  }
  * { margin: 0; padding: 0; box-sizing: border-box; }
  html, body {
    width: 1200px; height: 978px; overflow: hidden;
    background: var(--backdrop);
  }
  .postcard {
    position: absolute; left: 44px; top: 83px;
    width: 1096px; height: 802px;
    background: var(--mist);
    font-family: "Arimo", Arial, sans-serif;
  }
  .masthead {
    position: absolute; left: 0; top: 0; width: 100%; height: 210px;
    background: var(--gold);
  }
  .brand-name {
    position: absolute; left: 128px; top: 62px; width: 210px;
    color: var(--navy-ink); font-weight: 700; text-align: center;
    line-height: 1;
  }
  .brand-name .primary { display: block; font-size: 38px; letter-spacing: 1px; }
  .brand-name .secondary { display: block; font-size: 11px; letter-spacing: 2.4px; margin-top: 12px; }
  .slogan {
    position: absolute; left: 350px; top: 70px; width: 626px;
    font-family: "Gelasio", Georgia, serif;
    font-size: 40px; line-height: 50px; color: var(--heading-ink);
    text-align: center; text-transform: uppercase; font-weight: 400;
  }
  .limits-table {
    position: absolute; left: 60px; top: 257px; width: 975px;
    border-collapse: collapse; color: var(--white);
    font-size: 22px;
  }
  .limits-table th, .limits-table td {
    border: 2px solid var(--rule); height: 39px; padding: 0;
    text-align: center; vertical-align: middle;
  }
  .limits-table th {
    background: var(--taupe); font-weight: 700; height: 44px;
  }
  .limits-table .label { text-align: left; padding-left: 32px; }
  .limits-table th.label { text-align: center; padding-left: 0; }
  .limits-table .col-type { width: 429px; }
  .limits-table .col-year { width: 195px; }
  .limits-table .col-year.narrow { width: 181px; }
  .limits-table tr.dark td { background: var(--ocean); }
  .limits-table tr.light td { background: var(--teal); }
  .limits-table tr.tall td { height: 54px; }
  .limits-table tr.tall .label { line-height: 22px; }
  .footer-band {
    position: absolute; left: 0; bottom: 0; width: 100%; height: 130px;
  }
  .footer-band svg { position: absolute; left: 0; top: 0; }
  .contact {
    position: absolute; left: 56px; top: 37px;
    color: var(--white); font-size: 21px; line-height: 34px;
  }
  .contact .fax { margin-left: 14px; }
  .website {
    position: absolute; right: 60px; top: 42px;
    color: var(--white); font-size: 29px; font-weight: 700;
  }
</style>
</head>
<body>
  <div class="postcard">
    <header class="masthead">
      <div class="brand-name">
        <span class="primary">Bellwether</span>
        <span class="secondary">PENSION GROUP, INC.</span>
      </div>
      <h1 class="slogan">Providing and protecting<br>retirement since 1983</h1>
    </header>

    <table class="limits-table">
      <thead>
        <tr>
          <th class="label col-type">Type of Limitation</th>
          <th class="col-year">2015</th>
          <th class="col-year narrow">2014</th>
          <th class="col-year narrow">2013</th>
        </tr>
      </thead>
      <tbody>
        <tr class="dark"><td class="label">401(k) / 403 (b) Elective Deferrals</td><td>$18,000</td><td>$17,500</td><td>$17,500</td></tr>
        <tr class="light"><td class="label">Catch-up amount</td><td>$6,000</td><td>$5,500</td><td>$5,500</td></tr>
        <tr class="dark"><td class="label">Defined Benefit Plans</td><td>$210,000</td><td>$210,000</td><td>$205,000</td></tr>
        <tr class="light"><td class="label">Defined Contribution Plan</td><td>$53,000</td><td>$52,000</td><td>$51,000</td></tr>
        <tr class="dark"><td class="label">Annual Compensation Limit</td><td>$265,000</td><td>$260,000</td><td>$255,000</td></tr>
        <tr class="light"><td class="label">Highly Compensated Employees</td><td>$120,000</td><td>$115,000</td><td>$115,000</td></tr>
        <tr class="dark"><td class="label">Key employee officer threshold</td><td>$170,000</td><td>$170,000</td><td>$165,000</td></tr>
        <tr class="light tall"><td class="label">Income Subject to Social<br>Security Tax</td><td>$118,500</td><td>$117,000</td><td>$113,700</td></tr>
      </tbody>
    </table>

    <footer class="footer-band">
      <svg width="1096" height="130" viewBox="0 0 1096 130" aria-hidden="true">
        <rect x="0" y="0" width="1096" height="130" fill="var(--taupe)"/>
        <polygon points="0,0 611,0 741,130 0,130" fill="var(--ocean)"/>
      </svg>
      <address class="contact" style="font-style:normal">
        1840 Harbor View Ave., Suite 210, Redondo CA 90277<br>
        Phone: 310-555-0142 <span class="fax">Fax: 310-555-0178</span>
      </address>
      <div class="website">www.bellwetherpension.com</div>
    </footer>
  </div>
</body>
</html>
```